Dalton Power Supply, Inc. Business Card Design

We are an Electrical Distributor looking for a Modern, Professional Business Card design.

Target Market(s)

Residential Commercial Industrial

Industry/Entity Type

Electrical

Contact Information for Business Card

Dalton Power Supply, Inc.
418 Maple Ridge Lane
Brookvale, NC 27514
555-214-7630
555-214-8842 Fax
daltonpower@brightmail-example.net

```html
<!DOCTYPE html>
<html lang="en">
<head>
<meta charset="utf-8">
<title>Dalton Power Supply, Inc. – Business Card</title>
<link rel="stylesheet" href="https://fonts.googleapis.com/css2?family=Open+Sans:wght@400;600;700&display=swap">
<style>
  :root {
    --brand-red: #ec1c24;
    --brand-red-deep: #d3161e;
    --paper: #ffffff;
    --ink-grey: #6d6e71;
    --backdrop: #3a3440;
  }
  * { box-sizing: border-box; margin: 0; padding: 0; }
  html, body {
    width: 1200px; height: 800px; overflow: hidden;
    background: var(--backdrop);
    font-family: "Open Sans", Arial, sans-serif;
  }
  .stage { position: relative; width: 1200px; height: 800px; }
  .card {
    position: absolute; width: 540px; height: 308px;
    overflow: hidden; box-shadow: 0 6px 18px rgba(0,0,0,.35);
  }
  /* Front */
  .card-front { left: 330px; top: 50px; background: var(--brand-red); }
  .lockup { display: flex; align-items: center; gap: 14px; }
  .lockup-mark { border-radius: 50%; flex: none; }
  .lockup-name { font-weight: 700; line-height: 1; letter-spacing: -0.5px; }
  .lockup-sub { font-weight: 600; line-height: 1.1; }
  .card-front .lockup {
    position: absolute; left: 118px; top: 108px; color: var(--paper);
  }
  .card-front .lockup-mark { width: 92px; height: 92px; background: var(--paper); }
  .card-front .lockup-name { font-size: 58px; }
  .card-front .lockup-sub { font-size: 20px; margin-left: 4px; }
  /* Back */
  .card-back { left: 330px; top: 420px; background: var(--paper); display: flex; }
  .back-panel { position: relative; width: 46%; background: var(--brand-red); }
  .panel-circle {
    position: absolute; left: 62px; top: 32px; width: 130px; height: 130px;
    border-radius: 50%; background: var(--brand-red-deep);
  }
  .address {
    position: absolute; left: 26px; bottom: 34px; color: var(--paper);
    font-size: 12.5px; line-height: 1.35; font-style: normal;
  }
  .address .company { font-weight: 700; }
  .back-info { position: relative; flex: 1; }
  .card-back .lockup { position: absolute; left: 26px; top: 38px; color: var(--brand-red); gap: 9px; }
  .card-back .lockup-mark { width: 48px; height: 48px; background: var(--brand-red); }
  .card-back .lockup-name { font-size: 34px; }
  .card-back .lockup-sub { font-size: 12px; margin-left: 2px; }
  .person { position: absolute; right: 24px; top: 146px; text-align: right; }
  .person-name { color: var(--brand-red); font-size: 19px; font-weight: 400; }
  .person-title { color: var(--ink-grey); font-size: 13px; }
  .contacts {
    position: absolute; right: 24px; bottom: 22px; list-style: none;
    color: var(--ink-grey); font-size: 11.5px; text-align: right; line-height: 1.55;
  }
  .contacts li { display: flex; justify-content: flex-end; align-items: center; gap: 6px; }
  .contacts svg { width: 11px; height: 11px; fill: var(--brand-red); flex: none; }
</style>
</head>
<body>
<main class="stage">
  <section class="card card-front" aria-label="Card front">
    <div class="lockup">
      <span class="lockup-mark"></span>
      <div>
        <div class="lockup-name">Dalton</div>
        <div class="lockup-sub">Power Supply, Inc.</div>
      </div>
    </div>
  </section>

  <section class="card card-back" aria-label="Card back">
    <div class="back-panel">
      <span class="panel-circle"></span>
      <address class="address">
        <div class="company">Dalton Power Supply, Inc.</div>
        <div>418 Maple Ridge Lane</div>
        <div>Brookvale, NC 27514</div>
      </address>
    </div>
    <div class="back-info">
      <div class="lockup">
        <span class="lockup-mark"></span>
        <div>
          <div class="lockup-name">Dalton</div>
          <div class="lockup-sub">Power Supply, Inc.</div>
        </div>
      </div>
      <div class="person">
        <div class="person-name">Evan Holt</div>
        <div class="person-title">CEO</div>
      </div>
      <ul class="contacts">
        <li>555-214-7630
          <svg viewBox="0 0 16 16" aria-hidden="true"><path d="M3 1h3l1.5 4-2 1.2a9 9 0 0 0 4.3 4.3L11 8.5l4 1.5v3a2 2 0 0 1-2 2A13 13 0 0 1 1 3a2 2 0 0 1 2-2z"/></svg>
        </li>
        <li>555-214-8842 Fax
          <svg viewBox="0 0 16 16" aria-hidden="true"><path d="M4 1h8v4H4zM1 6h14v7h-3v2H4v-2H1zM5 10v4h6v-4z"/></svg>
        </li>
        <li>daltonpower@brightmail-example.net
          <svg viewBox="0 0 16 16" aria-hidden="true"><path d="M1 3h14v10H1zm1.5 1.2v.4L8 9l5.5-4.4v-.4z"/></svg>
        </li>
      </ul>
    </div>
  </section>
</main>
</body>
</html>
```